Design a Professional Stationery

Hi everyone,
I would like to make a design of stationery for my company Kestrel Wrap (www.kestrelwrap-example.com).
General Info: We are manufacturers of packaging supplies (poly bubble mailers, kraft bubble mailers, bubble wrap, tape, stretch film). We have couple of big warehouses in Los Angeles and New Jersey that serves East and West Coasts. We store lot of boxes with our product. We are wholesalers so we work with big serious distributors.

Project Goals: Create a business stationery that will look professional, modern and straight to the point. Colors: Dark blue, white, light blue (please see the web site). Blue is the color of success.
I want them to be presentable. As you might need to imagine my team will walk around the businesses and leave folders with information at clients table. We will distribute them at the trade shows, business meetings etc.
Updates

Target Market(s)

Business professionals looking for professional wholesaler manufacturer.

Industry/Entity Type

It Company

Font styles to use
Serif
Sans Serif

Colors
3276b5
0255a3
85acd3
cedeed
eaf1f7

Requirements
Must have
• People photos, product photos, add professional warehouse photos, truck, machinery.
Nice to have
• NLP
Should not have
• Use your imagination, no limits so far

```html
<!DOCTYPE html>
<html lang="en">
<head>
<meta charset="utf-8">
<title>Kestrel Wrap Presentation Folder</title>
<link rel="stylesheet" href="https://fonts.googleapis.com/css2?family=Cinzel:wght@600&family=Open+Sans:wght@400;600&display=swap">
<style>
  :root {
    --backdrop: #e6e6e6;
    --navy: #233a6a;
    --navy-deep: #1c3160;
    --pale: #eef2f7;
    --sky: #cedeed;
    --gold: #c9a23a;
  }
  * { box-sizing: border-box; margin: 0; padding: 0; }
  html, body { width: 1200px; height: 1000px; overflow: hidden; }
  body { background: var(--backdrop); position: relative; font-family: "Open Sans", sans-serif; }

  .folder { position: absolute; left: 180px; top: 220px; width: 840px; height: 560px; display: flex; box-shadow: 0 10px 30px rgba(0,0,0,.18); }
  .panel { position: relative; width: 420px; height: 560px; background: var(--navy); overflow: hidden; }
  .panel--back { border-right: 1px solid var(--navy-deep); }

  /* back cover contact strip */
  .contact-strip { position: absolute; left: 0; right: 0; top: 470px; height: 74px; display: flex; }
  .contact-card { width: 136px; background: var(--pale); padding: 12px 10px 8px; color: var(--navy); }
  .contact-card .brand-name { font-family: "Cinzel", serif; font-weight: 600; font-size: 11px; letter-spacing: .5px; color: var(--navy); margin-bottom: 6px; display: flex; align-items: center; gap: 4px; }
  .brand-mark { width: 6px; height: 6px; background: var(--navy); display: inline-block; }
  .contact-line { font-size: 4.6px; line-height: 8px; display: flex; align-items: center; gap: 3px; white-space: nowrap; }
  .contact-line svg { width: 6px; height: 6px; flex: none; }
  .contact-row { display: flex; gap: 6px; }
  .strip-photo { flex: 1; border-left: 2px solid var(--pale); }
  .photo-team { background: linear-gradient(135deg, #a58a6e, #d9c3a8 50%, #6f5c4b); }
  .photo-truck { background: linear-gradient(180deg, #7fa6d4 0%, #b7cde6 55%, #6e7a85 56%, #4d5660 100%); }
  .photo-forklift { background: linear-gradient(135deg, #8a7a63, #c59a52 45%, #4f5b68); }

  /* front cover header */
  .front-header { position: absolute; left: 0; top: 0; width: 420px; height: 220px; }
  .logo-block { position: absolute; left: 40px; top: 84px; }
  .logo-block .brand-name { font-family: "Cinzel", serif; font-weight: 600; font-size: 22px; color: var(--navy); letter-spacing: 1px; display: flex; align-items: center; gap: 8px; }
  .logo-block .brand-mark { width: 12px; height: 12px; }
  .tagline { font-size: 5.5px; font-weight: 600; color: var(--gold); letter-spacing: .8px; text-transform: uppercase; margin-top: 2px; }
</style>
</head>
<body>
  <main class="folder">
    <section class="panel panel--back">
      <div class="contact-strip">
        <div class="contact-card">
          <div class="brand-name"><span class="brand-mark"></span>Kestrel Wrap</div>
          <div class="contact-line">
            <svg viewBox="0 0 10 10"><rect width="10" height="10" fill="#233a6a"/><path d="M5 2 L8 5 V8 H2 V5 Z" fill="#fff"/></svg>
            1200 Harbor Ave, Millbrook, CA 90000
          </div>
          <div class="contact-row">
            <div class="contact-line">
              <svg viewBox="0 0 10 10"><rect width="10" height="10" fill="#233a6a"/><path d="M3 2 L4.5 3.5 L3.8 4.5 Q4.8 6 5.8 6.3 L6.5 5.5 L8 7 L7 8 Q3 7.5 2 3 Z" fill="#fff"/></svg>
              555-010-2391
            </div>
            <div class="contact-line">
              <svg viewBox="0 0 10 10"><rect width="10" height="10" fill="#233a6a"/><circle cx="5" cy="5" r="2.6" fill="none" stroke="#fff" stroke-width="1"/></svg>
              www.kestrelwrap-example.com
            </div>
          </div>
        </div>
        <div class="strip-photo photo-team" role="img" aria-label="Business team reviewing work at a laptop"></div>
        <div class="strip-photo photo-truck" role="img" aria-label="Delivery truck on an open highway"></div>
        <div class="strip-photo photo-forklift" role="img" aria-label="Forklift moving pallets in a warehouse"></div>
      </div>
    </section>

    <section class="panel panel--front">
      <svg class="front-header" viewBox="0 0 420 220">
        <defs>
          <linearGradient id="warehouseTone" x1="0" y1="0" x2="1" y2="1">
            <stop offset="0" stop-color="#c8cace"/>
            <stop offset=".55" stop-color="#a9a39b"/>
            <stop offset="1" stop-color="#8c7d74"/>
          </linearGradient>
          <linearGradient id="mailerTone" x1="0" y1="0" x2="1" y2="1">
            <stop offset="0" stop-color="#f4d98a"/>
            <stop offset="1" stop-color="#e5bd5a"/>
          </linearGradient>
        </defs>
        <g role="img" aria-label="Warehouse interior with shelving, pallets and red pallet trucks">
          <path d="M0 0 H420 V205 Q220 178 0 186 Z" fill="url(#warehouseTone)"/>
        </g>
        <path d="M0 28 L300 78 L118 186 Q60 184 0 186 Z" fill="#eef1f5"/>
        <g role="img" aria-label="Stack of yellow padded bubble mailers">
          <path d="M0 134 L124 134 L110 186 Q60 184 0 186 Z" fill="url(#mailerTone)"/>
        </g>
      </svg>
      <div class="logo-block">
        <div class="brand-name"><span class="brand-mark"></span>Kestrel Wrap</div>
        <div class="tagline">Shipping and Mailing Supply</div>
      </div>
    </section>
  </main>
</body>
</html>
```